Velvette by Monica Darsh business cards

I am after a business card that will fit the name of my business - velvette.
I want something classy and sexy and nothing tacky.
Ideas that I like are Zebra print backgrounds glitter back grounds
Two ideas I had were
1. Zebra print in black and white, the name Velvette by Monica Darsh and a shilouette of a woman laying on top of the name. Or instead of zebra a glitter background.
2. Idea very similar except for instead of a woman a pair of lips maybe a hot pink glitter or a gold glitter depending on background with the business name between the lips.
Or you can do something completely different.

Industry/Entity Type

Business

```html
<!DOCTYPE html>
<html lang="en">
<head>
<meta charset="utf-8">
<title>Velvette – Business Cards</title>
<link rel="stylesheet" href="https://fonts.googleapis.com/css2?family=Playfair+Display:ital,wght@0,700;1,700&display=swap">
<style>
  :root {
    --backdrop: #e9e4dc;
    --card-black: #120d08;
    --card-brown: #2a1e10;
    --glitter-gold: #6b4a1c;
    --gold: #c9a24a;
    --hot-pink: #e7208f;
  }
  * { margin: 0; padding: 0; box-sizing: border-box; }
  html, body {
    width: 1200px;
    height: 784px;
    overflow: hidden;
    background: var(--backdrop);
  }
  .card-set {
    position: absolute;
    inset: 0;
    display: flex;
    align-items: center;
    justify-content: center;
    gap: 40px;
  }
  .card {
    position: relative;
    width: 540px;
    height: 309px;
    border-radius: 4px;
    overflow: hidden;
    background: var(--card-black);
    box-shadow: 0 10px 28px rgba(0, 0, 0, 0.25);
  }
  .card__glitter {
    position: absolute;
    inset: 0;
    background:
      radial-gradient(ellipse at 50% 50%, var(--card-brown) 0%, rgba(18,13,8,0) 60%),
      radial-gradient(ellipse at 100% 0%, var(--glitter-gold) 0%, rgba(18,13,8,0) 45%),
      radial-gradient(ellipse at 0% 100%, var(--glitter-gold) 0%, rgba(18,13,8,0) 45%),
      var(--card-black);
  }
  .card__content {
    position: absolute;
    inset: 0;
    display: flex;
    align-items: center;
    justify-content: center;
  }
  .card--back .card__content {
    padding-bottom: 60px;
  }
  .card--front .card__content {
    padding-left: 40px;
  }
  .phone-number {
    font-family: "Playfair Display", Georgia, serif;
    font-style: italic;
    font-weight: 700;
    font-size: 34px;
    letter-spacing: 2px;
    color: var(--gold);
    white-space: nowrap;
  }
  .brand {
    display: flex;
    align-items: center;
    gap: 14px;
  }
  .brand__dot {
    width: 22px;
    height: 22px;
    border-radius: 50%;
    background: var(--hot-pink);
  }
  .brand__name {
    font-family: "Playfair Display", Georgia, serif;
    font-weight: 700;
    font-size: 64px;
    line-height: 1;
    color: var(--gold);
  }
</style>
</head>
<body>
  <main class="card-set">
    <section class="card card--back">
      <div class="card__glitter" role="img" aria-label="Black background with gold glitter sparkle pattern"></div>
      <div class="card__content">
        <p class="phone-number">1555 012 734</p>
      </div>
    </section>
    <section class="card card--front">
      <div class="card__glitter" role="img" aria-label="Black background with gold glitter sparkle pattern"></div>
      <div class="card__content">
        <div class="brand">
          <span class="brand__dot"></span>
          <h1 class="brand__name">Velvette</h1>
        </div>
      </div>
    </section>
  </main>
</body>
</html>
```